Investment company needing business card

We are wanting a business card which looks sharp and easy on the eye. We are thinking of having a business card with the logo embossed on it, to really make it stand out. We will only have a small amount of information of the business card, person's name, position, email address and phone number

Contact Information for Business Card

Danica Pruett
Executive Assistant
+64 21 547 3162
danicap@harwellcapital.co.nz

Requirements
Must have
• Embossed logo
Should not have
• Not to be busy

```html
<!DOCTYPE html>
<html lang="en">
<head>
<meta charset="utf-8">
<title>Harwell Capital — Business Card</title>
<link rel="stylesheet" href="https://fonts.googleapis.com/css2?family=Exo+2:wght@700;800&family=Lato:wght@400&display=swap">
<style>
  :root {
    --backdrop: #2b2b2c;
    --card: #111112;
    --card-edge: #1c1c1d;
    --accent: #21c07a;
    --grey: #8d8e90;
    --text-light: #d4d5d6;
    --rule: #4a4b4d;
  }
  * { margin: 0; padding: 0; box-sizing: border-box; }
  html, body {
    width: 1200px; height: 900px; overflow: hidden;
    background: var(--backdrop);
  }
  .canvas { position: relative; width: 1200px; height: 900px; }

  .card {
    position: absolute;
    width: 520px; height: 300px;
    background: linear-gradient(160deg, var(--card-edge), var(--card) 55%);
    box-shadow: 0 14px 30px rgba(0,0,0,0.45);
    overflow: hidden;
  }
  .card::after {
    content: ""; position: absolute; left: 0; right: 0; bottom: 0;
    height: 10px; background: var(--accent);
  }
  .card--front { left: 380px; top: 100px; }
  .card--back  { left: 300px; top: 470px; }

  .brand {
    display: flex; align-items: center; justify-content: center; gap: 14px;
  }
  .brand__square { width: 34px; height: 34px; background: var(--accent); }
  .brand__name {
    font-family: "Exo 2", sans-serif; font-weight: 800;
    font-size: 30px; letter-spacing: 2px; color: var(--accent);
    text-transform: uppercase;
  }
  .card--front .brand { position: absolute; left: 0; right: 0; top: 124px; }
  .card--back .brand { margin-top: 42px; }

  .contact { text-align: center; }
  .contact__name {
    margin-top: 36px;
    font-family: "Exo 2", sans-serif; font-weight: 800;
    font-size: 22px; letter-spacing: 1px; color: var(--accent);
    text-transform: uppercase;
  }
  .contact__rule {
    width: 220px; height: 1px; margin: 8px auto; background: var(--rule);
  }
  .contact__role {
    font-family: "Lato", sans-serif; font-size: 14px;
    color: var(--text-light); text-transform: uppercase; letter-spacing: 0.5px;
  }
  .contact__line {
    font-family: "Lato", sans-serif; font-size: 15px;
    color: var(--text-light); line-height: 1.5;
  }
  .contact__phone { margin-top: 4px; }
</style>
</head>
<body>
<main class="canvas">
  <section class="card card--front" aria-label="Card front">
    <div class="brand">
      <span class="brand__square"></span>
      <span class="brand__name">Harwell Capital</span>
    </div>
  </section>

  <section class="card card--back" aria-label="Card back">
    <div class="brand">
      <span class="brand__square"></span>
      <span class="brand__name">Harwell Capital</span>
    </div>
    <div class="contact">
      <p class="contact__name">Danica Pruett</p>
      <div class="contact__rule"></div>
      <p class="contact__role">Executive Assistant</p>
      <div class="contact__rule"></div>
      <p class="contact__line contact__phone">+64 21 547 3162</p>
      <p class="contact__line">danicap@harwellcapital.co.nz</p>
    </div>
  </section>
</main>
</body>
</html>
```